Veltrix inc. Aviation website

we are looking for a very modern and luxury web design, we are an aviation based company and specialize in aircraft exports and setup of air services world wide.
we want the website to be unique, creative, luxurious, professional, and to make an statement.
we have attached the logo.
our business cards theme is black background with gold stamping, if that is the rout you want to take.
**The format we are looking for is Wordpress.**
**the website is www.veltrixinc-example.com**
** 3 pages:
1. home page: -overview/about us
-industry leading
- worldwide presence
- aerial support
2. products and services: -business aircrafts
-commercial aircrafts
-amphibious aircrafts
-operation setup
-maintenance & crew training
3. contact us
**our location: Marlow Fenwick Harbour Airfield, Hangar 14**
we do appreciate suggestions
Thank you all.
Target Market(s)
Aviation professionals, Aircraft import/export, airlines, air taxi operations
Industry/Entity Type
It Company
Number of Pages Required
3 page
Requirements
Must have
- must have a very modern and luxurious design, and must be aviation oriented, and must have the logo, must be professional looking and be animated.
Nice to have
- black, gold, and burgandy colour
Should not have
- should not be playful and cartoony.

```html
<!DOCTYPE html>
<html lang="en">
<head>
<meta charset="utf-8">
<title>Veltrix inc. — Aviation</title>
<link href="https://fonts.googleapis.com/css2?family=Montserrat:wght@400;600;700&family=Open+Sans:wght@400;600&display=swap" rel="stylesheet">
<style>
:root{
  --red:#b3232d;
  --red-dark:#8e1a22;
  --gold:#c9a12a;
  --gold-dark:#a8831c;
  --ink:#2a2a2a;
  --muted:#8a8a8a;
  --light:#f2f2f2;
  --footer:#262626;
  --footer-bottom:#1b1b1b;
  --white:#fff;
}
*{box-sizing:border-box;margin:0;padding:0}
html,body{width:1200px;height:2988px;overflow:hidden}
body{font-family:"Open Sans",Arial,sans-serif;color:var(--ink);background:var(--white)}
h1,h2,h3,h4,.nav,.btn{font-family:"Montserrat",Arial,sans-serif}

.site-header{height:56px;display:flex;align-items:center;justify-content:space-between;padding:0 100px;background:var(--white)}
.brand{display:flex;align-items:center;gap:10px;font-family:"Montserrat",sans-serif;font-weight:700;font-size:24px;color:var(--red);letter-spacing:1px}
.brand-mark{width:22px;height:22px;border-radius:50%;background:var(--gold)}
.nav{display:flex;gap:26px;font-size:12px;font-weight:700;color:var(--ink)}
.nav a{color:inherit;text-decoration:none;padding:20px 0}
.nav a.active{color:var(--red);border-bottom:2px solid var(--red)}

.hero{position:relative;height:584px;background:linear-gradient(180deg,#4d6f8c 0%,#8fa7b8 40%,#c9cfc8 58%,#6b6e64 72%,#4a4d47 100%);text-align:center;color:var(--white)}
.hero h1{padding-top:244px;font-size:62px;font-weight:700;letter-spacing:1px}
.hero p{width:720px;margin:14px auto 0;font-size:17px;line-height:26px;opacity:.9}
.dots{position:absolute;bottom:12px;left:0;right:0;display:flex;justify-content:center;gap:6px}
.dots span{width:12px;height:12px;border-radius:50%;background:var(--white);opacity:.7}
.dots span:first-child{opacity:1;background:#ddd}

.overview{height:600px;text-align:center;padding-top:100px}
.section-title{font-size:44px;font-weight:400;color:var(--red)}
.overview .lead{width:680px;margin:24px auto 0;font-size:15px;line-height:24px;color:#555}
.features{display:flex;justify-content:center;gap:130px;margin-top:80px}
.feature{width:250px}
.feature-icon{width:120px;height:120px;border-radius:50%;margin:0 auto;display:flex;align-items:center;justify-content:center}
.feature h3{margin-top:24px;font-size:18px;font-weight:600;letter-spacing:.5px}
.feature p{margin-top:10px;font-size:13px;line-height:20px;color:var(--muted)}

.industry{height:400px;background:linear-gradient(135deg,var(--red) 0%,#c2434a 55%,var(--red-dark) 100%);text-align:center;color:var(--white);padding-top:64px}
.industry h2{font-size:46px;font-weight:400}
.industry p{width:800px;margin:24px auto 0;font-size:16px;line-height:26px;opacity:.9}
.btn{display:inline-block;font-size:14px;font-weight:600;letter-spacing:1px;text-decoration:none;color:var(--white)}
.btn-outline{margin-top:40px;border:2px solid var(--white);padding:10px 30px}

.presence{height:580px;padding-top:52px;position:relative}
.presence .section-title{text-align:center;color:var(--ink);font-size:42px}
.slider-arrows{position:absolute;right:100px;top:70px;display:flex;gap:8px}
.slider-arrows span{width:22px;height:22px;border-radius:50%;background:#ccc}
.posts{display:flex;gap:28px;padding:0 100px;margin-top:30px}
.post{width:316px}
.post-media{height:200px}
.post h4{margin-top:20px;font-size:16px;font-weight:600;line-height:22px;text-transform:uppercase}
.post p{margin-top:10px;font-size:13px;line-height:20px;color:var(--muted)}
.btn-gold{margin-top:16px;background:var(--gold);padding:9px 18px;font-size:13px}
.btn-red{background:var(--red)}

.aerial{height:420px;background:linear-gradient(180deg,var(--gold) 0%,#d2b03f 60%,var(--gold-dark) 100%);text-align:center;color:var(--white);padding-top:52px}
.aerial h2{font-size:46px;font-weight:400}
.aerial .lead{margin-top:12px;font-size:14px;opacity:.9}
.contact-form{width:1000px;margin:40px auto 0}
.form-row{display:flex;gap:20px}
.field{flex:1;height:40px;background:var(--white);border:0;font-family:inherit;font-size:13px;color:#999;padding:0 12px;display:flex;align-items:center}
.field.message{height:76px;margin-top:16px;align-items:flex-start;padding-top:10px}
.btn-submit{margin-top:22px;background:var(--red);padding:12px 40px;font-size:14px}

.site-footer{height:300px;background:var(--footer);color:#ccc;display:flex;gap:0;padding:60px 100px 0}
.footer-col{width:200px;font-size:13px;line-height:24px}
.footer-col h5{font-family:"Montserrat",sans-serif;font-size:15px;font-weight:600;color:var(--white);margin-bottom:14px;letter-spacing:.5px}
.contact-line{display:flex;align-items:center;gap:8px}
.social{display:flex;gap:8px;margin-top:12px}
.social span{width:28px;height:28px;border-radius:50%;background:#3f7fc2}
.social span:nth-child(4){background:var(--red)}
.footer-bottom{height:48px;background:var(--footer-bottom);color:#999;font-size:12px;display:flex;align-items:center;justify-content:space-between;padding:0 100px}
</style>
</head>
<body>

<header class="site-header">
  <div class="brand"><span class="brand-mark"></span>VELTRIX</div>
  <nav class="nav">
    <a class="active" href="#">HOME</a>
    <a href="#">ABOUT US</a>
    <a href="#">INDUSTRY</a>
    <a href="#">WORLDWIDE PRESENCE</a>
    <a href="#">AERIAL SUPPORT</a>
  </nav>
</header>

<section class="hero" role="img" aria-label="Jet airliner taking off over a runway under a cloudy sky">
  <h1>INDUSTRY LEADING</h1>
  <p>Trusted partner for aircraft export, fleet setup and global air service solutions that keep every operation flying.</p>
  <div class="dots"><span></span><span></span><span></span><span></span></div>
</section>

<section class="overview">
  <h2 class="section-title">Overview of Veltrix</h2>
  <p class="lead">VELTRIX delivers results. Our goal is to provide both a superior customer experience and tremendous value.</p>
  <div class="features">
    <div class="feature">
      <div class="feature-icon" style="background:var(--gold)">
        <svg width="60" height="60" viewBox="0 0 60 60"><circle cx="30" cy="30" r="20" fill="none" stroke="#fff" stroke-width="8" stroke-dasharray="8 5"/><circle cx="30" cy="30" r="8" fill="#fff"/></svg>
      </div>
      <h3>ENGINEERING</h3>
      <p>Sed ut perspiciatis unde omnis iste natus error sit voluptatem accusantium doloremque laudantium.</p>
    </div>
    <div class="feature">
      <div class="feature-icon" style="background:var(--red)">
        <svg width="60" height="60" viewBox="0 0 60 60"><path d="M30 6 L36 26 L54 38 L54 42 L36 36 L34 48 L40 54 L20 54 L26 48 L24 36 L6 42 L6 38 L24 26 Z" fill="#fff"/></svg>
      </div>
      <h3>TESTING</h3>
      <p>Sed ut perspiciatis unde omnis iste natus error sit voluptatem accusantium doloremque laudantium.</p>
    </div>
    <div class="feature">
      <div class="feature-icon" style="background:var(--ink)">
        <svg width="64" height="60" viewBox="0 0 64 60"><circle cx="32" cy="20" r="9" fill="#fff"/><rect x="18" y="33" width="28" height="18" rx="9" fill="#fff"/><circle cx="12" cy="26" r="6" fill="#fff"/><circle cx="52" cy="26" r="6" fill="#fff"/></svg>
      </div>
      <h3>TRAINING</h3>
      <p>Sed ut perspiciatis unde omnis iste natus error sit voluptatem accusantium doloremque laudantium.</p>
    </div>
  </div>
</section>

<section class="industry">
  <h2>Industry Leading</h2>
  <p>Lorem ipsum dolor sit amet, consectetur adipiscing elit, sed do eiusmod tempor incididunt ut labore et dolore magna aliqua.</p>
  <p>Duis aute irure dolor in reprehenderit in voluptate velit esse cillum dolore eu fugiat nulla pariatur. Excepteur sint occaecat cupidatat non proident.</p>
  <a class="btn btn-outline" href="#">READ MORE</a>
</section>

<section class="presence">
  <h2 class="section-title">Worldwide Presence</h2>
  <div class="slider-arrows"><span></span><span></span></div>
  <div class="posts">
    <article class="post">
      <div class="post-media" role="img" aria-label="City skyline with glass towers under a blue sky" style="background:linear-gradient(160deg,#6d9cc9,#c4d8e8 60%,#7e8c98)"></div>
      <h4>Excepteur sint occaecat cupidatat non proident</h4>
      <p>Sed ut perspiciatis unde omnis iste natus error sit voluptatem accusantium doloremque laudantium.</p>
      <a class="btn btn-gold" href="#">Read More ›</a>
    </article>
    <article class="post">
      <div class="post-media" role="img" aria-label="Aircraft landing over palm trees at sunset" style="background:linear-gradient(180deg,#e39a4a,#b85a2a 60%,#3a2418)"></div>
      <h4>Nemo enim ipsam voluptatem quia voluptas sit</h4>
      <p>Sed ut perspiciatis unde omnis iste natus error sit voluptatem accusantium doloremque laudantium.</p>
      <a class="btn btn-gold btn-red" href="#">Read More ›</a>
    </article>
    <article class="post">
      <div class="post-media" role="img" aria-label="Travellers enjoying a sunny city waterfront" style="background:linear-gradient(160deg,#8fb8dc,#d9c8a8 60%,#7a6a58)"></div>
      <h4>Quis autem vel eum iure reprehenderit qui</h4>
      <p>Sed ut perspiciatis unde omnis iste natus error sit voluptatem accusantium doloremque laudantium.</p>
      <a class="btn btn-gold" href="#">Read More ›</a>
    </article>
  </div>
</section>

<section class="aerial">
  <h2>Aerial Support</h2>
  <p class="lead">VELTRIX delivers results. Our goal is to provide both a superior customer experience and tremendous value.</p>
  <form class="contact-form">
    <div class="form-row">
      <div class="field">Name</div>
      <div class="field">Email</div>
      <div class="field">Phone</div>
      <div class="field">Interested in ▾</div>
    </div>
    <div class="field message">Message</div>
    <a class="btn btn-submit" href="#">SUBMIT NOW</a>
  </form>
</section>

<footer class="site-footer">
  <div class="footer-col">
    <h5>COMPANY</h5>
    Home<br>About Us<br>Industry Leading<br>Worldwide Presence<br>Aerial Support
  </div>
  <div class="footer-col">
    <h5>INFORMATION</h5>
    Engineering<br>Testing<br>Training<br>Others
  </div>
  <div class="footer-col" style="width:240px">
    <h5>GET IN TOUCH</h5>
    <div class="contact-line"><svg width="14" height="14" viewBox="0 0 14 14"><path d="M3 1 L5 1 L6 4 L4.5 5 Q6 8.5 9 9.5 L10 8 L13 9 L13 11 Q12 13 10 13 Q2 11 1 3 Q1 1 3 1Z" fill="#ccc"/></svg>Call us on +1 (555) 014 7781</div>
    <div class="contact-line"><svg width="14" height="14" viewBox="0 0 14 14"><rect x="1" y="3" width="12" height="8" fill="none" stroke="#ccc" stroke-width="1.4"/><path d="M1 3 L7 8 L13 3" fill="none" stroke="#ccc" stroke-width="1.4"/></svg>hello@veltrixinc-example.com</div>
  </div>
  <div class="footer-col" style="width:160px">
    <h5>WHY US</h5>
    Customers<br>Team<br>FAQ<br>Contact
  </div>
  <div class="footer-col">
    <h5>FOLLOW US</h5>
    Please connect with us on
    <div class="social"><span></span><span></span><span></span><span></span></div>
  </div>
</footer>
<div class="footer-bottom">
  <span>© 2016 Company Name. All right reserved. Term of Use</span>
  <span>↑ Top</span>
</div>

</body>
</html>
```